Lantern & Row Theatre Academy Business Card

We need a professional looking card for the Lantern & Row Theatre Academy. The logo is attached.
The owner is: Maribel Quistorp
Phone Number: 303-555-0147
Email: lrtheatreacademy@mailbox-demo.com
Website: lrtheatre-demo.com
Somewhere on the front of the card we would like to see the slogan: Step into the limelight
On the back we would like to see the quote: All the world's a stage. -Edmund Pelgrave
We are open to different colors for the wording or maybe just black. Something that will go well with the logo.
Target Market(s)
Individuals seeking a professional children's theatre.
Industry/Entity Type
Business
Colors
Look and feel

```html
<!DOCTYPE html>
<html lang="en">
<head>
<meta charset="utf-8">
<title>Lantern &amp; Row Theatre Academy – Business Card</title>
<link rel="stylesheet" href="https://fonts.googleapis.com/css2?family=Questrial&family=Open+Sans:wght@700&display=swap">
<style>
  :root {
    --backdrop: #efefef;
    --card-white: #ffffff;
    --brand-red: #861316;
    --curtain-bright: #e3181d;
    --curtain-mid: #b50f14;
    --curtain-dark: #3a0204;
    --ink: #111111;
    --quote-ink: #ffffff;
  }
  html, body {
    margin: 0;
    padding: 0;
    width: 1200px;
    height: 720px;
    overflow: hidden;
    background: var(--backdrop);
  }
  .canvas {
    position: relative;
    width: 1200px;
    height: 720px;
    display: flex;
    align-items: center;
    justify-content: center;
    gap: 40px;
  }
  .card {
    position: relative;
    width: 540px;
    height: 309px;
    background: var(--card-white);
    box-shadow: 0 2px 8px rgba(0,0,0,0.12);
    overflow: hidden;
  }

  /* Back of card */
  .card-back__curtain {
    position: absolute;
    inset: 0;
    background:
      radial-gradient(ellipse 60% 70% at 50% 50%, var(--curtain-bright) 0%, var(--curtain-mid) 55%, transparent 100%),
      linear-gradient(90deg, var(--curtain-dark) 0%, var(--curtain-mid) 18%, var(--curtain-bright) 50%, var(--curtain-mid) 82%, var(--curtain-dark) 100%);
  }
  .card-back__quote {
    position: absolute;
    inset: 0;
    display: flex;
    align-items: center;
    justify-content: center;
    margin: 0;
    font-family: "Open Sans", sans-serif;
    font-weight: 700;
    font-size: 15px;
    color: var(--quote-ink);
    letter-spacing: 0.1px;
  }

  /* Front of card */
  .brand {
    position: absolute;
    left: 48px;
    top: 58px;
    display: flex;
    align-items: center;
    gap: 10px;
  }
  .brand__mark {
    width: 16px;
    height: 16px;
    background: var(--brand-red);
  }
  .brand__name {
    font-family: "Questrial", sans-serif;
    font-size: 21px;
    color: var(--brand-red);
    margin: 0;
  }
  .slogan {
    position: absolute;
    left: 74px;
    top: 100px;
    margin: 0;
    font-family: "Questrial", sans-serif;
    font-size: 13px;
    color: var(--ink);
  }
  .owner {
    position: absolute;
    right: 32px;
    top: 142px;
    text-align: center;
  }
  .owner__name {
    margin: 0;
    font-family: "Questrial", sans-serif;
    font-size: 17px;
    color: var(--brand-red);
  }
  .owner__title {
    margin: 2px 0 0;
    font-family: "Questrial", sans-serif;
    font-size: 12px;
    color: var(--ink);
  }
  .contact-band {
    position: absolute;
    left: 0;
    right: 0;
    bottom: 18px;
    height: 72px;
    background: var(--brand-red);
    display: flex;
    justify-content: space-between;
    align-items: flex-start;
    padding: 10px 16px 0 22px;
    box-sizing: border-box;
    font-family: "Questrial", sans-serif;
    font-size: 10.5px;
    line-height: 1.9;
    color: var(--ink);
  }
  .contact-band p { margin: 0; }
  .contact-band__web { text-align: center; }
</style>
</head>
<body>
  <main class="canvas">
    <section class="card card-back">
      <div class="card-back__curtain" role="img" aria-label="Red theatre stage curtain backdrop"></div>
      <p class="card-back__quote">All the world's a stage -Edmund Pelgrave</p>
    </section>

    <section class="card card-front">
      <div class="brand">
        <span class="brand__mark"></span>
        <p class="brand__name">Lantern &amp; Row Theatre Academy</p>
      </div>
      <p class="slogan">Step into the limelight</p>
      <div class="owner">
        <p class="owner__name">Maribel Quistorp</p>
        <p class="owner__title">Owner</p>
      </div>
      <div class="contact-band">
        <p class="contact-band__address">412 North West Larkmoor,<br>Fenbrook, NY 55501</p>
        <p class="contact-band__phone">P: 303-555-0147</p>
        <p class="contact-band__web">lrtheatreacademy@mailbox-demo.com<br>lrtheatre-demo.com</p>
      </div>
    </section>
  </main>
</body>
</html>
```